Magnetic Business Card Design. One sided

Not happy yet with a design yet currently winning so far are the designs 5162585 5135573 5132280

Logo
unmatched Quality through traditional friendly service" sound like a good line. Blockages, Hot water units & all plumbing services.
7days,
free quote: 0491 275 634
Maybe put on it: Qualified, Licensed
www.brighttapplumbing.example.au

Make word as big so it is clearly able to be read

BrightTap Plumbing PTY LTD, target market is the middle aged mostly woman professional that owns a house and would rather pay a professional to do the job rather then a handyman.
We are a plumbing company based in Melbourne small and family owned with a focus on service to our customers.

I am after a design that is clean, professional and appealing to the eye which fits with the visual appearance of my web site and logo.

Our most profitable jobs are blockages and hot water units. however we do all types of plumbing. Maybe a point to make on the cards not sure tho.

I have included our previous magnet that i had designed with a pixel press template. if you can improve what we say to get new customers or totally change what is on the magnet. that would be fantastic.

I will also include other marketing material i have previously used

"unmatched Quality Through traditional friendly service" Could be a good catch line

These magnets are dropped into thousands of letter boxes and hopefully will find there way onto new clients fridges. Fridges in million dollar plus houses.

I really look forward to seeing your design. Thank you

Contact Information for Business Card

Number: 0491 275 634
Web site: www.Brighttapplumbing.example.au

```html
<!DOCTYPE html>
<html lang="en">
<head>
<meta charset="utf-8">
<title>BrightTap Plumbing – Magnet Card</title>
<link rel="stylesheet" href="https://fonts.googleapis.com/css2?family=Oswald:wght@700&family=Montserrat:wght@700&family=Raleway:wght@400&family=Lora:wght@700&display=swap">
<style>
  :root {
    --backdrop: #d9d6d2;
    --card: #ffffff;
    --navy: #1e1b5c;
    --blue: #2254a8;
    --band: #151515;
    --band-text: #ffffff;
    --rule: #3a6fc4;
  }
  * { margin: 0; padding: 0; box-sizing: border-box; }
  html, body {
    width: 1200px;
    height: 1200px;
    overflow: hidden;
    background: var(--backdrop);
  }
  .canvas {
    width: 1200px;
    height: 1200px;
    display: flex;
    align-items: center;
    justify-content: center;
  }
  .magnet-card {
    position: relative;
    width: 1104px;
    height: 684px;
    background: var(--card);
    box-shadow: 0 6px 18px rgba(0,0,0,0.25);
  }
  .brand-since {
    position: absolute;
    top: 34px; left: 0; right: 0;
    text-align: center;
    font-family: "Lora", serif;
    font-weight: 700;
    font-size: 36px;
    line-height: 1;
    color: var(--blue);
  }
  .brand-name {
    position: absolute;
    top: 110px; left: 0; right: 0;
    text-align: center;
    white-space: nowrap;
    font-family: "Oswald", sans-serif;
    font-weight: 700;
    font-size: 124px;
    line-height: 1.2;
    color: var(--navy);
    letter-spacing: 1px;
  }
  .phone-row {
    position: absolute;
    top: 392px; left: 0; right: 0;
    display: flex;
    align-items: center;
    justify-content: center;
    gap: 22px;
  }
  .phone-icon { width: 86px; height: 76px; }
  .phone-number {
    font-family: "Oswald", sans-serif;
    font-weight: 700;
    font-size: 96px;
    line-height: 1.05;
    color: var(--navy);
    letter-spacing: 1px;
    white-space: nowrap;
  }
  .website {
    position: absolute;
    top: 512px; left: 0; right: 0;
    text-align: center;
    white-space: nowrap;
    font-family: "Montserrat", sans-serif;
    font-weight: 700;
    font-size: 42px;
    line-height: 1.2;
    color: var(--blue);
  }
  .service-band {
    position: absolute;
    left: 0; right: 0; bottom: 0;
    height: 100px;
    background: var(--band);
    border-top: 2px solid var(--rule);
    display: flex;
    align-items: center;
    justify-content: center;
    text-align: center;
    font-family: "Raleway", sans-serif;
    font-weight: 400;
    font-size: 26px;
    line-height: 1.4;
    color: var(--band-text);
  }
</style>
</head>
<body>
<main class="canvas">
  <section class="magnet-card">
    <p class="brand-since">Since 1980</p>
    <h1 class="brand-name">BrightTap Plumbing</h1>
    <div class="phone-row">
      <svg class="phone-icon" viewBox="0 0 86 76" aria-hidden="true">
        <path d="M6 26 C6 12 24 6 43 6 C62 6 80 12 80 26 L80 32 L62 32 L62 24 C56 21 30 21 24 24 L24 32 L6 32 Z" fill="var(--navy)"/>
        <path d="M26 30 L60 30 L74 58 L74 70 L12 70 L12 58 Z" fill="var(--navy)"/>
        <circle cx="43" cy="52" r="11" fill="#fff"/>
        <circle cx="43" cy="52" r="5" fill="var(--navy)"/>
      </svg>
      <span class="phone-number">0491 275 634</span>
    </div>
    <p class="website">www.Brighttapplumbing.example.au</p>
    <footer class="service-band">
      <p>All Plumbing and gas fitting. 7 day quick, affordable, reliable service<br>through traditional friendly service</p>
    </footer>
  </section>
</main>
</body>
</html>
```